Business to Business Website Homepage Design

Hi, My Web Developer is giving me designs that aren't quite taking my fancy as far as visual impact. I'd love to see designs come out which are simple, fresh and powerful.
I just want a PDF document that I can give to my web developer to follow, so this project is NOT to make a website, its to design the homepage.
I would like it to scroll down through different areas of my website on the homepage. Our colours are Blood Orange, White, Grey & Black.
I like these websites:
Simplicity
https://www.quenvalo.com/au/webapps/mpp/home
Our Team Section
http://trelmicode.com.au/
We'd like our logo on top left. Nav bar top right. Have an image which we can place a headline subject on + video icon which will pop out with a video and opt in for name and email with a heading so people know what they're opting in for.
The next section should have a lot of white space, this "What we do" which is 1) Grow in size so your business can get bigger 2) increase in value, so you maximise what your business is worth 3) Free up your time, so you can live the lifestyle you've always wanted. Our brief was we want image/text combo with a lot of white space,
Then we have our services
After Services, would like to have a "Why Work With Us" section
Then a testimonials section
Then "Our Team"
Then contact us.
Thats pretty much it, we'd just love some different ideas, these guys are almost there, but just need more impact.
Updates
Target Market(s)
Business Owners between $1m to $3m turnover
Industry/Entity Type
Business
Number of Pages Required
1 page
Look and feel
Each slider illustrates characteristics of the customer's brand and the style your logo design should communicate.

```html
<!DOCTYPE html>
<html lang="en">
<head>
<meta charset="utf-8">
<title>Tessmond Group — Home</title>
<link href="https://fonts.googleapis.com/css2?family=Open+Sans:wght@400;600;700;800&display=swap" rel="stylesheet">
<style>
:root{
  --orange:#e8491d;
  --orange-dark:#c93a12;
  --gold:#e0a11a;
  --blue:#1d7fd8;
  --ink:#222222;
  --charcoal:#2d2d2d;
  --grey:#6b6b6b;
  --white:#ffffff;
}
*{box-sizing:border-box;margin:0;padding:0}
html,body{width:1200px;height:4724px;overflow:hidden}
body{font-family:"Open Sans",Arial,sans-serif;color:var(--ink);background:var(--white);position:relative}
section,header,footer{position:relative;width:1200px;overflow:hidden}
.bg{position:absolute;inset:0}
.inner{position:relative;z-index:1}

/* header + hero */
.hero{height:610px;color:var(--white)}
.hero .bg{background:linear-gradient(120deg,#3a3c40 0%,#595a5c 45%,#8b8884 70%,#4b4c4e 100%)}
.hero .bg::after{content:"";position:absolute;inset:0;background:rgba(20,20,22,.45)}
.topbar{position:absolute;top:0;left:0;right:0;height:86px;z-index:2;display:flex;align-items:center;justify-content:space-between;padding:0 90px;background:rgba(255,255,255,.96)}
.brand{display:flex;align-items:center;gap:12px;font-weight:700;font-size:24px;color:var(--orange);letter-spacing:1px;text-transform:uppercase}
.brand-dot{width:34px;height:34px;border-radius:50%;background:var(--orange)}
.nav{display:flex;height:86px}
.nav a{display:flex;align-items:center;padding:0 30px;font-size:15px;color:var(--ink);text-decoration:none}
.nav a.active{background:var(--orange);color:var(--white)}
.hero-copy{position:absolute;top:300px;left:0;right:0;text-align:center;z-index:1}
.hero-copy h1{font-size:40px;font-weight:700;letter-spacing:1px}
.hero-copy h1 span{color:var(--orange)}
.play{margin:30px auto 0;width:92px;height:92px;border-radius:50%;border:4px solid var(--white);display:flex;align-items:center;justify-content:center}

/* what we do */
.grow{height:350px;background:var(--white)}
.rocket{position:absolute;left:160px;top:60px;width:260px;height:240px;border-radius:50%;background:radial-gradient(circle at 55% 40%,#f46a3c 0%,#f4b23c 35%,#eaeaea 70%,#ffffff 100%)}
.feature-copy{position:absolute;width:560px}
.grow .feature-copy{right:90px;top:50px;text-align:right}
.feature-copy h2{font-size:30px;font-weight:800;text-transform:uppercase}
.feature-copy .sub{font-size:24px;margin-bottom:22px}
.feature-copy p{font-size:13px;line-height:1.7;color:var(--grey);margin-bottom:14px}
.value{height:350px;color:var(--white)}
.value .bg{background:linear-gradient(100deg,var(--orange) 0%,#e0531f 55%,var(--orange-dark) 100%)}
.value .feature-copy{left:90px;top:70px;width:1020px}
.value .feature-copy p{color:#ffe2d6}
.freetime{height:400px;color:var(--white)}
.freetime .bg{background:linear-gradient(90deg,#575757 0%,#3c3c3c 50%,#2a2a2a 100%)}
.freetime .feature-copy{right:90px;top:60px;width:1000px;text-align:right}
.freetime .feature-copy p{color:#d7d7d7}

/* services */
.services{height:400px;background:var(--blue);color:var(--white)}
.section-title{text-align:center;font-size:30px;font-weight:800;text-transform:uppercase;padding-top:45px}
.services-grid{display:grid;grid-template-columns:repeat(3,1fr);gap:40px 40px;padding:45px 90px 0}
.service{display:flex;gap:18px}
.service-icon{flex:0 0 78px;height:78px;border-radius:50%;border:3px solid var(--white);display:flex;align-items:center;justify-content:center}
.service h3{font-size:15px;font-weight:700;text-transform:uppercase;margin-bottom:6px}
.service p{font-size:12px;line-height:1.55;color:#dcecfb}

/* why */
.why{height:375px;color:var(--white)}
.why .bg{background:linear-gradient(100deg,#6fb43a 0%,#3fa46a 35%,#2f8fc0 70%,#2468b8 100%)}
.why .intro{text-align:center;font-size:13px;line-height:1.6;width:760px;margin:16px auto 0;color:#eaf6ea}
.stats{display:flex;justify-content:space-between;padding:40px 170px 0}
.stat{text-align:center;width:160px}
.stat-icon{margin:0 auto 8px;width:44px;height:44px}
.stat strong{display:block;font-size:48px;font-weight:700;line-height:1.1}
.stat span{font-size:14px;text-transform:uppercase;letter-spacing:1px}

/* testimonials */
.testimonials{height:420px;color:var(--white)}
.testimonials .bg{background:linear-gradient(180deg,#3b3b3b 0%,#262626 100%)}
.avatar{margin:28px auto 0;width:110px;height:110px;border-radius:50%;border:4px solid var(--white);background:linear-gradient(160deg,#cfb7a0,#8e7766)}
.quote{position:relative;width:860px;margin:30px auto 0;text-align:center;font-size:17px;line-height:1.65;color:#e4e4e4}
.quote-mark{position:absolute;left:-60px;top:-20px;font-size:90px;font-weight:800;color:var(--white);line-height:1}
.quote-name{text-align:center;margin-top:18px;font-size:18px}

/* team */
.team{height:655px;background:var(--white)}
.team .section-title{color:var(--ink);padding-top:30px}
.team-grid{display:grid;grid-template-columns:repeat(4,300px);grid-auto-rows:280px;margin-top:38px}
.member{background:linear-gradient(180deg,#e9e9e9,#bdbdbd)}
.member:nth-child(2n){background:linear-gradient(180deg,#d9d9d9,#a9a9a9)}

/* contact */
.contact{height:990px;color:var(--white)}
.contact .bg{background:linear-gradient(180deg,#3a3a3a 0%,#242424 100%)}
.quote-form{position:absolute;left:85px;top:120px;width:570px;height:725px;background:var(--orange-dark);border:6px solid var(--gold);padding:40px 44px}
.quote-form h3{font-size:24px;font-weight:700;margin-bottom:30px}
.field{height:44px;background:var(--white);color:#8a8a8a;font-size:14px;padding:12px 16px;margin-bottom:18px}
.field.tall{height:260px}
.submit{display:inline-block;background:var(--charcoal);color:var(--white);font-weight:700;padding:14px 40px;font-size:15px;text-transform:uppercase}
.info{position:absolute;left:775px;top:120px;width:350px}
.info h3{font-size:24px;font-weight:700;margin-bottom:36px}
.info-row{display:flex;gap:16px;align-items:flex-start;font-size:15px;line-height:1.5;margin-bottom:22px;color:#e7e7e7}
.socials{display:flex;gap:12px;margin-top:10px}
.socials span{width:40px;height:40px;border-radius:50%;background:var(--blue)}
.mail-art{position:absolute;left:880px;top:500px;width:220px;height:190px;border-radius:12px;background:linear-gradient(150deg,#6fb3ea,#1f74c8)}
.contact-band{position:absolute;left:0;right:0;bottom:0;height:60px;background:var(--orange)}

/* footer */
.site-footer{height:164px;background:var(--white);padding:40px 90px 0}
.footer-links{display:flex;gap:26px;font-size:14px;color:var(--grey)}
.footer-bottom{display:flex;justify-content:space-between;align-items:center;margin-top:26px}
.footer-bottom .brand{font-size:18px}
.footer-bottom .brand-dot{width:24px;height:24px}
.copyright{font-size:13px;color:var(--grey)}
.footer-socials{display:flex;gap:10px}
.footer-socials span{width:28px;height:28px;border-radius:50%;background:var(--orange)}
</style>
</head>
<body>

<section class="hero">
  <div class="bg" role="img" aria-label="Photo of a smiling businessman at work in a bright office"></div>
  <header class="topbar">
    <div class="brand"><span class="brand-dot"></span>Tessmond Group</div>
    <nav class="nav">
      <a class="active" href="#">Home</a><a href="#">Services</a><a href="#">Clients</a><a href="#">Jobs</a><a href="#">Contact Us</a>
    </nav>
  </header>
  <div class="hero-copy">
    <h1>WELCOME ON <span>TESSMOND GROUP</span></h1>
    <div class="play"><svg width="34" height="38" viewBox="0 0 34 38"><path d="M4 2 L32 19 L4 36 Z" fill="#fff"/></svg></div>
  </div>
</section>

<section class="grow">
  <div class="rocket" role="img" aria-label="Illustration of a rocket launching with a trail of flame"></div>
  <div class="feature-copy">
    <h2>Grow in size</h2>
    <div class="sub">so your business can get bigger</div>
    <p>We help established owners build the structure, people and systems needed to scale with confidence. Our advisers work beside you to spot new openings, remove bottlenecks and turn steady revenue into lasting growth across every part of your operation, month after month.</p>
    <p>Every plan is tailored to your goals, so the path to a bigger business stays clear, practical and measurable.</p>
  </div>
</section>

<section class="value">
  <div class="bg"></div>
  <div class="feature-copy">
    <h2>Increase in value</h2>
    <div class="sub">so you maximise what your business is worth</div>
    <p>A valuable business is one that runs well without you. We strengthen margins, document processes and build a team that delivers, so buyers and investors see a dependable asset. Whether you plan to sell, grow or pass it on, we position your company to command the highest possible price.</p>
  </div>
</section>

<section class="freetime">
  <div class="bg" role="img" aria-label="Photo of a relaxed couple enjoying time outdoors"></div>
  <div class="feature-copy">
    <h2>Free up your time</h2>
    <div class="sub">so you can live the lifestyle you've always wanted</div>
    <p>Too many owners are trapped working in the business instead of on it. We help you delegate with confidence, set clear responsibilities and build reporting you can trust, so the daily grind no longer depends on you alone being there every single day.</p>
    <p>The result is more hours for family, travel and the things that matter most, while your company keeps moving forward steadily and your results keep improving.</p>
  </div>
</section>

<section class="services">
  <h2 class="section-title">Our Services</h2>
  <div class="services-grid">
    <div class="service">
      <div class="service-icon"><svg width="36" height="36" viewBox="0 0 36 36" fill="none" stroke="#fff" stroke-width="3"><circle cx="18" cy="11" r="7"/><path d="M4 34c0-8 6-13 14-13s14 5 14 13"/></svg></div>
      <div><h3>People</h3><p>Recruit, train and keep a team that shares your vision and delivers results every day.</p></div>
    </div>
    <div class="service">
      <div class="service-icon"><svg width="38" height="38" viewBox="0 0 38 38" fill="none" stroke="#fff" stroke-width="3"><circle cx="19" cy="19" r="7"/><path d="M19 3v6M19 29v6M3 19h6M29 19h6M7.7 7.7l4.2 4.2M26.1 26.1l4.2 4.2M7.7 30.3l4.2-4.2M26.1 11.9l4.2-4.2"/></svg></div>
      <div><h3>Business Systems</h3><p>Clear processes and tools that let your business run smoothly without constant supervision.</p></div>
    </div>
    <div class="service">
      <div class="service-icon"><svg width="34" height="38" viewBox="0 0 34 38" fill="none" stroke="#fff" stroke-width="3"><path d="M25 9c-2-3-5-4-8-4-4 0-8 2-8 6 0 9 17 5 17 14 0 4-4 6-9 6-4 0-7-2-9-5M17 1v36"/></svg></div>
      <div><h3>Funding</h3><p>Access the right capital at the right time to support expansion and new investment.</p></div>
    </div>
    <div class="service">
      <div class="service-icon"><svg width="38" height="34" viewBox="0 0 38 34" fill="none" stroke="#fff" stroke-width="3"><path d="M3 29l10-10 7 6 14-16M26 9h8v8"/></svg></div>
      <div><h3>New Earning Streams</h3><p>Find extra revenue lines that build on your strengths and reach new buyers.</p></div>
    </div>
    <div class="service">
      <div class="service-icon"><svg width="38" height="38" viewBox="0 0 38 38" fill="none" stroke="#fff" stroke-width="3"><circle cx="19" cy="19" r="15"/><path d="M4 19h30M19 4c-6 8-6 22 0 30M19 4c6 8 6 22 0 30"/></svg></div>
      <div><h3>New Markets</h3><p>Enter new regions and sectors with research and plans that reduce the risk.</p></div>
    </div>
    <div class="service">
      <div class="service-icon"><svg width="38" height="34" viewBox="0 0 38 34" fill="none" stroke="#fff" stroke-width="3"><rect x="3" y="10" width="32" height="21" rx="2"/><path d="M13 10V5h12v5M3 19h32"/></svg></div>
      <div><h3>New Businesses</h3><p>Launch or acquire ventures that add value to the group you already own.</p></div>
    </div>
  </div>
</section>

<section class="why">
  <div class="bg" role="img" aria-label="Blurred photo of a team meeting tinted in green and blue"></div>
  <div class="inner">
    <h2 class="section-title">Why Work With Us</h2>
    <p class="intro">We have guided hundreds of owners through growth, sale and succession. Our track record speaks for itself, and our clients keep coming back because the advice works in the real world.</p>
    <div class="stats">
      <div class="stat"><svg class="stat-icon" viewBox="0 0 44 44" fill="none" stroke="#fff" stroke-width="3"><circle cx="22" cy="14" r="8"/><path d="M6 42c0-9 7-15 16-15s16 6 16 15"/></svg><strong>235</strong><span>Followers</span></div>
      <div class="stat"><svg class="stat-icon" viewBox="0 0 44 44" fill="none" stroke="#fff" stroke-width="3"><circle cx="22" cy="22" r="18"/><path d="M22 11v11l8 5"/></svg><strong>1980</strong><span>Since</span></div>
      <div class="stat"><svg class="stat-icon" viewBox="0 0 44 44" fill="none" stroke="#fff" stroke-width="3"><circle cx="22" cy="22" r="18"/><path d="M14 26c2 4 5 6 8 6s6-2 8-6M16 17h1M27 17h1"/></svg><strong>221</strong><span>Happy Clients</span></div>
      <div class="stat"><svg class="stat-icon" viewBox="0 0 44 44" fill="none" stroke="#fff" stroke-width="3"><rect x="6" y="8" width="32" height="30" rx="2"/><path d="M14 23l6 6 11-12"/></svg><strong>365</strong><span>Projects</span></div>
    </div>
  </div>
</section>

<section class="testimonials">
  <div class="bg"></div>
  <div class="inner">
    <h2 class="section-title">Our Testimonials</h2>
    <div class="avatar" role="img" aria-label="Portrait photo of the client giving the testimonial"></div>
    <div class="quote"><span class="quote-mark">“</span>Working with the team changed how I run my company. Within a year our revenue grew, my managers took real ownership and I finally stepped back from the daily rush. I now spend weekends with my kids and still see better results than ever before.</div>
    <div class="quote-name">Tobias Renfrew, Father</div>
  </div>
</section>

<section class="team">
  <h2 class="section-title">Our Team</h2>
  <div class="team-grid">
    <div class="member" role="img" aria-label="Team member portrait photo"></div>
    <div class="member" role="img" aria-label="Team member portrait photo"></div>
    <div class="member" role="img" aria-label="Team member portrait photo"></div>
    <div class="member" role="img" aria-label="Team member portrait photo"></div>
    <div class="member" role="img" aria-label="Team member portrait photo"></div>
    <div class="member" role="img" aria-label="Team member portrait photo"></div>
    <div class="member" role="img" aria-label="Team member portrait photo"></div>
    <div class="member" role="img" aria-label="Team member portrait photo"></div>
  </div>
</section>

<section class="contact">
  <div class="bg"></div>
  <div class="inner"><h2 class="section-title">Contact Us</h2></div>
  <form class="quote-form">
    <h3>Get a free quote</h3>
    <div class="field">Your Name</div>
    <div class="field">Email Address</div>
    <div class="field">Phone Number</div>
    <div class="field tall">Message</div>
    <span class="submit">Send</span>
  </form>
  <div class="info">
    <h3>Contact Information</h3>
    <div class="info-row"><svg width="22" height="26" viewBox="0 0 22 26"><path d="M11 1C5.5 1 2 5 2 10c0 7 9 15 9 15s9-8 9-15c0-5-3.5-9-9-9z" fill="#fff"/><circle cx="11" cy="10" r="3.5" fill="#2d2d2d"/></svg><span>27 Larkspur Street,<br>Fernvale, VIC 3411</span></div>
    <div class="info-row"><svg width="22" height="18" viewBox="0 0 22 18" fill="none" stroke="#fff" stroke-width="2"><rect x="1" y="1" width="20" height="16" rx="1"/><path d="M1 2l10 8 10-8"/></svg><span>hello@tessmondgroup.com</span></div>
    <div class="info-row"><svg width="22" height="22" viewBox="0 0 22 22"><path d="M5 1l4 5-2 3c1 3 3 5 6 6l3-2 5 4-2 4C10 21 1 12 1 3z" fill="#fff"/></svg><span>(03) 8127 4410</span></div>
    <div class="socials"><span></span><span></span><span></span></div>
  </div>
  <div class="mail-art" role="img" aria-label="Illustration of an envelope with a phone receiver"></div>
  <div class="contact-band"></div>
</section>

<footer class="site-footer">
  <div class="footer-links"><span>Home</span><span>Services</span><span>Clients</span><span>Jobs</span><span>Contact Us</span></div>
  <div class="footer-bottom">
    <div class="brand"><span class="brand-dot"></span>Tessmond Group</div>
    <div class="copyright">Copyright © Tessmond Group 2024. All rights reserved.</div>
    <div class="footer-socials"><span></span><span></span><span></span><span></span></div>
  </div>
</footer>

</body>
</html>
```